Talvoro Equity LLC

Need Professional Business cards for New Investment Fund

Target Market(s)

High Quality investors

Industry/Entity Type

Financial

Contact Information for Business Card

Phone Number +1 555 284 6190
Name Milan Dorovsky
Title Fund Manager
email md@FundTalvoro.com
Website www.FundTalvoro.com

Colors

Designer to choose colors to be used in the design.

Requirements
Must have
• Must have our Logo and all of the above. Must be made so lettering and loge can be raised

```html
<!DOCTYPE html>
<html lang="en">
<head>
<meta charset="utf-8">
<title>Talvoro Equity – Business Card</title>
<link href="https://fonts.googleapis.com/css2?family=Jost:wght@500&family=Roboto:wght@400;500&display=swap" rel="stylesheet">
<style>
  :root {
    --backdrop: #c9c9c9;
    --forest: #38433b;
    --lime: #8cc11f;
    --paper: #f4f4f4;
    --ink: #3a3f3b;
    --ink-soft: #4a4f4b;
    --white: #f2f2f2;
  }
  * { margin: 0; padding: 0; box-sizing: border-box; }
  html, body { width: 1200px; height: 1138px; overflow: hidden; }
  body {
    background: var(--backdrop);
    position: relative;
    font-family: "Roboto", Arial, sans-serif;
  }
  .card {
    position: absolute;
    width: 620px;
    height: 374px;
    border-radius: 16px;
    overflow: hidden;
  }
  .card-front { left: 274px; top: 186px; background: var(--forest); }
  .card-back { left: 276px; top: 608px; background: var(--paper); }

  .brand {
    position: absolute;
    display: flex;
    align-items: center;
    gap: 12px;
    font-family: "Jost", "Futura", sans-serif;
    font-weight: 500;
    letter-spacing: 1px;
    line-height: 1;
  }
  .brand-mark { background: var(--lime); display: block; }
  .card-front .brand {
    left: 0; right: 0; top: 160px;
    justify-content: center;
    font-size: 58px;
    color: var(--white);
  }
  .card-front .brand-mark { width: 30px; height: 30px; }
  .card-back .brand {
    left: 36px; top: 112px;
    font-size: 50px;
    color: var(--forest);
  }
  .card-back .brand-mark { width: 26px; height: 26px; }

  .holder { position: absolute; left: 36px; top: 276px; }
  .holder-name { font-size: 23px; font-weight: 500; color: var(--ink); }
  .holder-title { font-size: 16px; color: var(--ink-soft); margin-top: 7px; }

  .contacts { position: absolute; left: 346px; top: 242px; list-style: none; }
  .contacts li {
    display: flex; align-items: center; gap: 16px;
    font-size: 16px; color: var(--ink); height: 24px;
  }
  .contacts svg { width: 14px; height: 14px; fill: var(--lime); }

  .card-footer { position: absolute; left: 0; bottom: 0; width: 620px; height: 48px; }
  .tagline {
    position: absolute; right: 34px; bottom: 16px;
    font-size: 15.5px; color: var(--white);
  }
</style>
</head>
<body>
  <section class="card card-front">
    <div class="brand"><span class="brand-mark"></span>TALVORO</div>
  </section>

  <section class="card card-back">
    <div class="brand"><span class="brand-mark"></span>TALVORO</div>

    <div class="holder">
      <p class="holder-name">Milan Dorovsky</p>
      <p class="holder-title">Fund Manager</p>
    </div>

    <ul class="contacts">
      <li>
        <svg viewBox="0 0 16 16" aria-hidden="true"><path d="M3 2h3l1 3-2 1a9 9 0 0 0 5 5l1-2 3 1v3a1 1 0 0 1-1 1A13 13 0 0 1 2 3a1 1 0 0 1 1-1z"/></svg>
        +1 555 284 6190
      </li>
      <li>
        <svg viewBox="0 0 16 16" aria-hidden="true"><path d="M1 3h14v10H1z M2 4l6 5 6-5" stroke="#f4f4f4" stroke-width="1"/></svg>
        md@FundTalvoro.com
      </li>
      <li>
        <svg viewBox="0 0 16 16" aria-hidden="true"><circle cx="8" cy="8" r="7"/><path d="M1 8h14M8 1c-3 4-3 10 0 14M8 1c3 4 3 10 0 14" stroke="#f4f4f4" stroke-width="0.8" fill="none"/></svg>
        www.FundTalvoro.com
      </li>
    </ul>

    <svg class="card-footer" viewBox="0 0 620 48" aria-hidden="true">
      <rect x="0" y="36" width="300" height="12" fill="var(--lime)"/>
      <path d="M290 48 L316 0 H620 V48 Z" fill="var(--forest)"/>
    </svg>
    <p class="tagline">Talvoro Equity | Steady Returns</p>
  </section>
</body>
</html>
```